Modern CNC Machining Facility in Need of Web Site Improvement

Brixton Fabrication and Tooling, LLC is in need of a web site update. We need to highlight both product sales and our manufacturing services offered. We have recently started offering online product sales and need a better ecommerce platform for our customers. We would like the design winner to be able to freelance the project to a fully functioning webpage.
www.brixtonfabrication.example
What we like about our current web site:
Black and red highlight colors
Gear and caliper logo
RNVR Veteran owned business
What we don't like about our current web site:
Unorganized
Doesn't stand out
Looks like it was made in 1995
Online Product sales are awkward

```html
<!DOCTYPE html>
<html lang="en">
<head>
<meta charset="utf-8">
<title>Brixton Fabrication and Tooling, LLC</title>
<link href="https://fonts.googleapis.com/css2?family=Open+Sans:wght@300;400;600;700&display=swap" rel="stylesheet">
<style>
:root{
  --red:#b3121a;
  --red-dark:#8f0f14;
  --ink:#333;
  --grey:#666;
  --light:#f4f4f4;
  --footer:#4a4a4a;
  --dot:#cfcfcf;
}
*{box-sizing:border-box;margin:0;padding:0}
html,body{width:1115px;height:1200px;overflow:hidden;background:#fff}
body{font-family:'Open Sans',sans-serif;color:var(--ink)}
.page{position:absolute;left:3px;top:0;width:1200px;height:1300px;transform:scale(0.923);transform-origin:0 0;
  background:linear-gradient(#ececec 0,#fff 110px,#fff 100%)}
.abs{position:absolute}
.brand{left:120px;top:20px;display:flex;align-items:center;gap:12px}
.brand-mark{width:78px;height:78px;border-radius:50%;background:var(--red);border:6px solid #2a2a2a}
.brand-name{font-size:21px;font-weight:400;color:var(--red);letter-spacing:.2px}
.utility{right:128px;top:14px;font-size:11px;color:var(--red);display:flex;gap:14px}
.follow{left:954px;top:44px;font-size:16px;color:#666}
.social{left:955px;top:68px;display:flex;gap:8px}
.social span{width:25px;height:25px;border:1px solid #ccc;border-radius:2px;background:linear-gradient(#fafafa,#ddd)}
.nav{left:120px;top:112px;width:961px;height:37px;border-radius:3px;background:linear-gradient(#555,#222);display:flex;align-items:center}
.nav .home{width:80px;height:37px;background:var(--red);border-radius:3px 0 0 3px;display:flex;align-items:center;justify-content:center}
.nav a{color:#fff;text-decoration:none;font-size:13px;padding:0 10px;height:37px;line-height:37px;border-right:1px solid #666}
.nav a.first{padding-left:20px}
.nav a.last{border-right:none}
.search{left:851px;top:118px;width:214px;height:25px;background:#fff;border-radius:3px;font-size:11px;color:#aaa;padding:5px 9px}
.search svg{position:absolute;right:8px;top:6px}
.hero{left:120px;top:158px;width:961px;height:343px;border-radius:3px;
  background:radial-gradient(circle at 72% 55%,#7a6a52 0,#4b3f31 25%,#2a241d 55%,#141210 100%)}
.caption{left:120px;top:227px;width:370px;height:216px;background:rgba(20,20,20,.78);padding:12px 25px;color:#fff}
.caption h1{font-size:26px;font-weight:400;line-height:28px}
.caption p{font-size:13px;line-height:16px;margin-top:18px}
.btn-more{position:absolute;left:23px;top:168px;width:121px;height:36px;background:var(--red);border-radius:4px;color:#fff;font-size:15px;font-weight:700;text-align:center;line-height:36px}
.dots{left:537px;top:485px;width:122px;height:35px;border-radius:18px;background:linear-gradient(#fff,#ddd);box-shadow:0 2px 4px rgba(0,0,0,.25);display:flex;align-items:center;justify-content:center;gap:11px}
.dots span{width:14px;height:14px;border-radius:50%;background:#444}
.dots span.on{background:var(--red)}
.rule{left:120px;width:961px;border-top:3px dotted var(--dot)}
.welcome{left:120px;top:553px;width:961px;text-align:center}
.welcome h2{font-size:30px;font-weight:400;color:var(--red);line-height:34px}
.welcome h3{font-size:17px;font-weight:700;color:#555;line-height:18px;margin-top:1px}
.welcome p{font-size:14px;font-weight:300;color:#555;line-height:19px;margin:18px 14px 0}
.section-title{left:132px;top:755px;font-size:24px;font-weight:700;color:var(--red)}
.card{top:826px;width:225px;height:232px;background:var(--light);border:1px solid #ddd}
.card .photo{height:170px}
.card .name{text-align:center;font-size:15px;color:#444;margin-top:5px}
.card .add{position:absolute;left:57px;top:200px;width:110px;height:26px;background:var(--red);color:#fff;font-size:12px;line-height:26px;padding-left:7px;border-radius:2px}
.card .add i{position:absolute;right:6px;top:4px;width:20px;height:18px;background:#fff;border-radius:1px}
.footer{left:120px;top:1092px;width:961px;height:200px;background:var(--footer);border-radius:4px 4px 0 0;color:#fff}
.col{position:absolute;top:27px;font-size:12px;line-height:18px}
.col h4{font-size:12px;font-weight:700;margin-bottom:4px}
.contact li{list-style:none;display:flex;gap:7px;margin-bottom:5px}
.contact svg{flex:none;margin-top:2px}
.col ul{list-style:none}
.copy{left:12px;top:176px;font-size:11.5px}
.legal{right:10px;top:176px;font-size:11.5px}
</style>
</head>
<body>
<div class="page">
  <div class="abs brand"><div class="brand-mark"></div><div class="brand-name">BRIXTON FABRICATION</div></div>
  <div class="abs utility"><span>ACCOUNT</span><span>|</span><span>CART TOTAL:&nbsp; $0.00</span></div>
  <div class="abs follow">Follow Us</div>
  <div class="abs social"><span></span><span></span><span></span><span></span></div>

  <nav class="abs nav">
    <div class="home"><svg width="22" height="20" viewBox="0 0 22 20"><path d="M11 1 1 10h3v9h5v-6h4v6h5v-9h3z" fill="#fff"/></svg></div>
    <a class="first">Online Products Sales</a><a>ICE Fishing Spears</a><a>About Us</a><a>Equipment</a><a class="last">Contact Us</a>
  </nav>
  <div class="abs search">Search...<svg width="16" height="14" viewBox="0 0 16 14"><circle cx="6" cy="6" r="4.5" fill="none" stroke="#aaa" stroke-width="2"/><path d="M9.5 9l5 4" stroke="#aaa" stroke-width="2.5"/></svg></div>

  <div class="abs hero" role="img" aria-label="Close-up photograph of interlocking brass and steel machine gears"></div>
  <div class="abs caption">
    <h1>Brixton Fabrication and Tooling, LLC</h1>
    <p>Lorem ipsum dolor sit amet, consectetur adipisicing elit, sed do eiusmod tempor incididunt ut labore et dolore magna aliqua.Ut enim ad minim veniam, quis nostrud exercitation ullamco.</p>
    <div class="btn-more">READ MORE</div>
  </div>
  <div class="abs dots"><span class="on"></span><span></span><span></span><span></span></div>

  <div class="abs rule" style="top:542px"></div>
  <div class="abs welcome">
    <h2>WELCOME TO BRIXTON FABRICATION</h2>
    <h3>LOREM IPSUM - DOLOR SIT AMET CONSECTETUR ADIPISICING ELIT,</h3>
    <p>Sed ut perspiciatis unde omnis iste natus error sit voluptatem accusantium doloremque laudantium, totam rem aperiam, eaque ipsa quae ab illo inventore veritatis et quasi architecto beatae vitae dicta sunt explicabo. Sed ut perspiciatis unde omnis iste natus error sit voluptatem Nemo enim ipsam voluptatem quia voluptas sit aspernatur aut odit aut fugit sed quia consequuntur magni dolores eos qui ratione voluptatem sequi nesciunt.</p>
    <p>Sed ut perspiciatis unde omnis iste natus error sit voluptatem Nemo enim ipsam voluptatem quia voluptas sit aspernatur aut odit aut fugit, sed quia consequuntur magni dolores eos qui ratione voluptatem sequi nesciunt.</p>
  </div>

  <div class="abs section-title">PRODUCTS</div>
  <div class="abs rule" style="top:789px"></div>

  <div class="abs card" style="left:121px"><div class="photo" role="img" aria-label="Photo of a silver clock face layered over gears" style="background:linear-gradient(135deg,#d6d6d6,#8a8a8a 60%,#bdbdbd)"></div><div class="name">Triple Gear Clock</div><div class="add">Add To Cart<i></i></div></div>
  <div class="abs card" style="left:366px"><div class="photo" role="img" aria-label="Photo of a small copper gear clock with wings resting on stones" style="background:linear-gradient(135deg,#9a8e80,#7a7065 55%,#b0a595)"></div><div class="name">Gear Clock with Wings</div><div class="add">Add To Cart<i></i></div></div>
  <div class="abs card" style="left:611px"><div class="photo" role="img" aria-label="Photo of a tall metal thermometer with a deer scene" style="background:linear-gradient(180deg,#ababab,#a2a39a)"></div><div class="name">Deer Thermometer</div><div class="add">Add To Cart<i></i></div></div>
  <div class="abs card" style="left:856px"><div class="photo" role="img" aria-label="Photo of a round wall clock with a dark sunburst frame" style="background:linear-gradient(180deg,#dcdcdc,#c9c6bd)"></div><div class="name">Sun Clock</div><div class="add">Add To Cart<i></i></div></div>

  <footer class="abs footer">
    <div class="col contact" style="left:13px">
      <h4>CONTACT US</h4>
      <ul>
        <li><svg width="14" height="14" viewBox="0 0 14 14"><rect width="14" height="14" rx="2" fill="#fff"/><path d="M7 2a3 3 0 0 0-3 3c0 2.5 3 6 3 6s3-3.5 3-6a3 3 0 0 0-3-3z" fill="#4a4a4a"/></svg><span>2140 Millrace Rd Hollis MI<br>,48012</span></li>
        <li><svg width="14" height="14" viewBox="0 0 14 14"><rect width="14" height="14" rx="2" fill="#fff"/><path d="M4 2h2l1 3-1.5 1a6 6 0 0 0 2.5 2.5L9 7l3 1v2c0 1-1 2-2 2C6 12 2 8 2 4c0-1 1-2 2-2z" fill="#4a4a4a"/></svg><span>555-014-2290</span></li>
        <li><svg width="14" height="14" viewBox="0 0 14 14"><rect width="14" height="14" rx="2" fill="#fff"/><path d="M2.5 4h9v6h-9zM2.5 4l4.5 3.5L11.5 4" fill="none" stroke="#4a4a4a" stroke-width="1.3"/></svg><span>Sales@BrixtonFabrication.example</span></li>
      </ul>
    </div>
    <div class="col" style="left:302px;font-size:13px"><h4 style="font-size:12px">COMPANY INFO</h4><ul><li>Home</li><li>Online Products Sales</li><li>ICE Fishing Spears</li><li>About Us</li><li>Equipment</li><li>Contact Us</li></ul></div>
    <div class="col" style="left:540px"><h4>SERVICES</h4><ul><li>Lorem Ipsum Dolor</li><li>Sit Amet Consectetuer</li><li>Adipisicing Elit</li><li>Lorem Ipsum Dolor</li><li>Sit Amet Consectetuer</li><li>Adipisicing Elit</li></ul></div>
    <div class="col" style="left:788px"><h4>SCHEDULE</h4><ul><li>Lorem Ipsum Dolor</li><li>Sit Amet Consectetuer</li><li>Adipisicing Elit</li></ul></div>
    <div class="abs copy">Copyright© 2014 Brixton Fabrication. All Rights Reserved</div>
    <div class="abs legal">Terms &amp; Condition &nbsp;|&nbsp; Privacy Policy</div>
  </footer>
</div>
</body>
</html>
```